Landing Page Design for Adult Dating Age Verification (18+)

The objective of this task is to design a visually appealing pre-landing page for the adult dating site "Plumvelle (site: https://plumvelle.example/)" with an age verification mechanism. The pre-landing page will feature two buttons that redirect visitors to the main offer. The design should also include a footer block that includes links to the terms of use, privacy policy, and contact us pages.

Design Requirements:
Develop an age verification section prominently displayed on the pre-landing page.
Design the section to include two buttons labeled "Yes" and "No" for visitors to confirm their age.
Ensure the section is visually appealing and clearly communicates the purpose of age verification.

Visual Appeal:
Create a visually appealing design that aligns with the branding and theme of the "Plumvelle" adult dating site.
Use suitable color schemes, typography, and graphics to enhance the overall visual appeal of the pre-landing page.

Layout and Navigation:
Design an engaging and intuitive layout that encourages visitors to interact with the page and proceed to the main offer.
Ensure clear and visible navigation elements that direct visitors to the main offer or provide additional information.

Responsive Design:
Develop a responsive design that provides a seamless user experience across various devices, including desktop and mobile.
Ensure the design elements and layout adapt well to different screen sizes and resolutions.

File Formats and Assets:
Deliver the final design in PSD, AI, or Sketch format, ensuring that the files are well-organized and layered.
Include any necessary images or assets used in the design, ensuring they are of high quality and optimized for web use.

```html
<!DOCTYPE html>
<html lang="en">
<head>
<meta charset="utf-8">
<title>Plumvelle – Age Verification</title>
<link rel="stylesheet" href="https://fonts.googleapis.com/css2?family=Barlow+Condensed:wght@300;600;700&family=Montserrat:wght@500&family=Lora:wght@600&display=swap">
<style>
  :root {
    --bg-dark: #262626;
    --bg-mid: #3a3a3a;
    --bg-light: #555555;
    --text: #ffffff;
    --text-soft: #e6e6e6;
    --accent-green: #4fb857;
    --brand-pink: #d7b3da;
    --dash: rgba(255,255,255,0.75);
  }
  * { margin: 0; padding: 0; box-sizing: border-box; }
  html, body { width: 1200px; height: 669px; overflow: hidden; }
  body {
    position: relative;
    font-family: "Barlow Condensed", sans-serif;
    color: var(--text);
    background: var(--bg-dark);
  }
  .hero-photo {
    position: absolute; inset: 0;
    background:
      radial-gradient(ellipse 45% 40% at 75% 85%, var(--bg-light) 0%, transparent 70%),
      radial-gradient(ellipse 50% 45% at 20% 70%, #4a4340 0%, transparent 70%),
      linear-gradient(160deg, var(--bg-mid) 0%, var(--bg-dark) 55%, #303030 100%);
  }
  .brand {
    position: absolute; left: 0; right: 0; top: 230px;
    display: flex; justify-content: center; align-items: center; gap: 6px;
  }
  .brand-dot { width: 20px; height: 20px; border-radius: 50%; background: var(--brand-pink); }
  .brand-name {
    font-family: "Lora", serif; font-weight: 600; font-size: 17px; color: var(--text);
  }
  .age-question {
    position: absolute; left: 69px; top: 282px; width: 1061px; height: 64px;
    border: 1px dashed var(--dash);
    display: flex; align-items: center; justify-content: center;
    font-size: 45px; font-weight: 300; letter-spacing: 0.5px; line-height: 1;
    text-transform: uppercase;
  }
  .age-question strong { font-weight: 700; margin: 0 10px; }
  .notice {
    position: absolute; left: 0; right: 0; top: 361px;
    text-align: center; font-size: 13px; font-weight: 300; color: var(--text-soft);
    text-transform: uppercase;
  }
  .choices {
    position: absolute; top: 417px; left: 249px;
    display: flex; gap: 12px;
  }
  .choice {
    width: 345px; height: 36px;
    display: flex; align-items: center; justify-content: center;
    font-family: "Barlow Condensed", sans-serif; font-weight: 600; font-size: 13.5px;
    text-transform: uppercase; letter-spacing: 0.3px;
    color: var(--text); text-decoration: none;
  }
  .choice--yes { background: var(--accent-green); }
  .choice--no { border: 1px solid var(--text); }
  .legal {
    position: absolute; left: 0; right: 0; top: 474px;
    text-align: center;
    font-family: "Montserrat", sans-serif; font-weight: 500; font-size: 7.5px;
    text-transform: uppercase; color: var(--text-soft);
  }
  .legal a { color: inherit; text-decoration: none; }
</style>
</head>
<body>
  <div class="hero-photo" role="img" aria-label="Dimmed photo of a woman in black lace lingerie lying on white bed sheets"></div>

  <div class="brand">
    <span class="brand-dot"></span>
    <span class="brand-name">Plumvelle</span>
  </div>

  <h1 class="age-question">Are you <strong>at least 18</strong> years old</h1>

  <p class="notice">You cannot access this website if you are under 18 years old.</p>

  <div class="choices">
    <a class="choice choice--yes" href="https://plumvelle.example/">I am over 18 years</a>
    <a class="choice choice--no" href="#">I am under 18 years</a>
  </div>

  <p class="legal">By entering this site you are agreeing to the <a href="#">terms of use</a> and <a href="#">privacy policy</a>.</p>
</body>
</html>
```